I need a business card design for a new counselling practice in Canberra, Australia. The name of the practice is Dr Grant Holloway, Counselling Services and the practice focuses on philosophical, narrative and existential counselling for individuals, couples and families. The final design should communicate professionalism, sophistication of analysis and psychological wholeness. The reverse side of the card should have an appointment reminder

Could the following qualifications also be included on card. BSc (Psychology), BA hons (Philosophy), PhD (Philosophy), Diploma of Community Counselling And the following affiliation Wellspring Guild of Talk Therapists and Allied Carers Inc. (WEGOTAC) And my contact phone mobile phone number is 0493817254, and email is Grant.Holloway347@mailbox-example.net for inclusion as well.

Thank you all who have put in a design so far. I just wanted to clarify some design points based on what you have submitted. 1. The Wellspring Guild of Talk Therapists. Allied Carers Inc. (WEGOTAC) is an affiliation only. 'Member of the Wellspring Guild of Talk Therapists. Allied Carers Inc (WEGOTAC)' should appear with the same prominence of a qualification. 2. The Post Graduate Diploma in Community Counselling is a quaification and should appear as 'PG Dip (Community Counselling)' after the other qualifications. 3. I am advertising myself as a counsellor so 'Dr Grant Holloway, Counselling Services' or 'Dr Grant Holloway, Counsellor' is the equivalent of the business name. After looking at some of the designs I prefer Dr Grant Holloway in sentence case rather than all capitals (DR GRANT HOLLOWAY). 4. 'Philosophical, narrative and existential counselling for individuals, couples and families' is the description of the type of counselling services and should appear on the card.

One further point. I have updated my email address for the card. It is now drgrantholloway@tallowfieldtherapy.org

```html
<!DOCTYPE html>
<html lang="en">
<head>
<meta charset="utf-8">
<title>Dr Grant Holloway, Counselling Services – Business Card</title>
<link rel="stylesheet" href="https://fonts.googleapis.com/css2?family=Cinzel:wght@400;700&family=Marcellus&family=Lato:wght@400;700;900&display=swap">
<style>
  :root {
    --backdrop: #2a2a2a;
    --card: #ffffff;
    --card-shade: #f1f1f1;
    --accent: #c8161d;
    --ink: #1f1f1f;
    --muted: #444444;
    --rule: #3a3a3a;
    --box: #555555;
  }
  * { box-sizing: border-box; margin: 0; padding: 0; }
  html, body {
    width: 1200px;
    height: 997px;
    overflow: hidden;
    background: var(--backdrop);
  }
  .canvas {
    position: relative;
    width: 1200px;
    height: 997px;
  }
  .card {
    position: absolute;
    width: 560px;
    height: 320px;
    border-radius: 18px;
    background: linear-gradient(160deg, var(--card) 0%, var(--card) 60%, var(--card-shade) 100%);
    box-shadow: 0 18px 40px rgba(0,0,0,0.55);
    overflow: hidden;
  }

  /* ---------- Appointment side ---------- */
  .card--appointment { left: 60px; top: 110px; }
  .appt-title {
    position: absolute;
    top: 26px; left: 0; right: 0;
    text-align: center;
    font-family: "Cinzel", serif;
    font-size: 17px;
    color: var(--accent);
    text-decoration: underline;
    text-underline-offset: 4px;
    letter-spacing: 0.5px;
  }
  .rule {
    position: absolute;
    height: 2px;
    background: var(--rule);
  }
  .label {
    position: absolute;
    font-family: "Lato", sans-serif;
    font-weight: 700;
    color: var(--accent);
  }
  .label--name { top: 92px; left: 0; right: 0; text-align: center; font-size: 14px; }
  .days {
    position: absolute;
    top: 142px; left: 34px; right: 34px;
    display: flex;
    justify-content: space-between;
  }
  .choice {
    display: flex;
    align-items: center;
    gap: 6px;
    font-family: "Lato", sans-serif;
    font-weight: 700;
    font-size: 14px;
    color: var(--accent);
  }
  .choice__box {
    width: 18px; height: 18px;
    border: 2px solid var(--box);
    border-radius: 4px;
    box-shadow: inset 0 1px 2px rgba(0,0,0,0.2);
  }
  .label--date { top: 196px; left: 34px; font-size: 16px; }
  .label--time { top: 196px; left: 290px; font-size: 16px; }
  .ampm {
    position: absolute;
    top: 194px; right: 34px;
    display: flex; gap: 16px;
  }
  .label--notes { top: 246px; left: 250px; font-size: 13px; font-weight: 400; }

  /* ---------- Details side ---------- */
  .card--details { left: 580px; top: 500px; }
  .practitioner {
    position: absolute;
    top: 26px; left: 36px;
    font-family: "Marcellus", serif;
    font-weight: 400;
    font-size: 27px;
    color: var(--accent);
    letter-spacing: 0.5px;
  }
  .qualifications {
    position: absolute;
    top: 66px; left: 36px;
    font-family: "Lato", sans-serif;
    font-weight: 900;
    font-size: 11.5px;
    line-height: 1.5;
    color: var(--ink);
  }
  .services {
    position: absolute;
    top: 138px; left: 36px; right: 36px;
    text-align: right;
    font-family: "Marcellus", serif;
    font-size: 15px;
    line-height: 1.55;
    color: var(--muted);
    text-decoration: underline;
    text-underline-offset: 4px;
    text-decoration-thickness: 1px;
  }
  .accent-rule {
    position: absolute;
    top: 200px; left: 36px; right: 36px;
    height: 2px;
    background: var(--accent);
  }
  .contact {
    position: absolute;
    left: 36px; bottom: 26px;
    list-style: none;
    font-family: "Lato", sans-serif;
    font-weight: 700;
    font-size: 15px;
    color: var(--ink);
  }
  .contact__item {
    display: flex;
    align-items: center;
    gap: 10px;
    margin-top: 8px;
  }
  .contact__icon { width: 18px; height: 18px; fill: var(--accent); flex: none; }
</style>
</head>
<body>
<main class="canvas">

  <section class="card card--appointment" aria-label="Appointment card">
    <h2 class="appt-title">Appointment Card</h2>
    <div class="rule" style="top:84px;left:34px;right:34px;"></div>
    <p class="label label--name">Patient Name</p>

    <div class="days">
      <span class="choice">Mon <span class="choice__box"></span></span>
      <span class="choice">Tue <span class="choice__box"></span></span>
      <span class="choice">Wed <span class="choice__box"></span></span>
      <span class="choice">Thu <span class="choice__box"></span></span>
      <span class="choice">Fri <span class="choice__box"></span></span>
      <span class="choice">Sat <span class="choice__box"></span></span>
    </div>

    <p class="label label--date">Date:</p>
    <div class="rule" style="top:220px;left:34px;width:236px;"></div>
    <p class="label label--time">Time:</p>
    <div class="rule" style="top:220px;left:290px;width:100px;"></div>
    <div class="ampm">
      <span class="choice">AM <span class="choice__box"></span></span>
      <span class="choice">PM <span class="choice__box"></span></span>
    </div>

    <p class="label label--notes">Notes:</p>
    <div class="rule" style="top:272px;left:34px;right:34px;"></div>
  </section>

  <section class="card card--details" aria-label="Business card">
    <h1 class="practitioner">Dr Grant Holloway</h1>
    <p class="qualifications">
      BSc (Psychology), BA hons (Philosophy), PhD (Philosophy),<br>
      PG Dip (Community Counselling)<br>
      Member of the Wellspring Guild of Talk Therapists.<br>
      Allied Carers Inc (WEGOTAC)
    </p>
    <p class="services">
      Philosophical, narrative and existential counselling<br>
      for individuals, couples and families
    </p>
    <div class="accent-rule"></div>
    <ul class="contact">
      <li class="contact__item">
        <svg class="contact__icon" viewBox="0 0 24 24" aria-hidden="true">
          <path d="M6.6 10.8c1.4 2.8 3.8 5.1 6.6 6.6l2.2-2.2c.3-.3.7-.4 1-.2 1.1.4 2.3.6 3.6.6.6 0 1 .4 1 1V20c0 .6-.4 1-1 1C10.6 21 3 13.4 3 4c0-.6.4-1 1-1h3.5c.6 0 1 .4 1 1 0 1.3.2 2.5.6 3.6.1.3 0 .7-.2 1l-2.3 2.2z"/>
        </svg>
        0493817254
      </li>
      <li class="contact__item">
        <svg class="contact__icon" viewBox="0 0 24 24" aria-hidden="true">
          <path d="M2 5h20v14H2z M3.5 6.5 12 13l8.5-6.5" fill="var(--accent)" stroke="#fff" stroke-width="1.4"/>
        </svg>
        drgrantholloway@tallowfieldtherapy.org
      </li>
    </ul>
  </section>

</main>
</body>
</html>
```